Silver Brook Custom Homes business card. Double sided. Modern. professional

Silver Brook Custom Homes
contemporary modern design with our logo /
Double sided with all our contact information
Use same Green colors as in our Logo. Contemporary logo that grabs your attention. Visually pleasing and balanced. Easy to read, and Vibrant. Would love an option for rounded edges. Embossed logo would be amazing.
Contact Information for Business Card
Dana Pellman Owner / General Contractor Silver Brook Custom Homes p: 555.555.0142 m: 555.555.0178 e: silverbrookcustomhomes@mailnest.example w: www.silverbrookcustomhomes.example 218 Wrenfield Mill Road Alderwick, ST 29088

```html
<!DOCTYPE html>
<html lang="en">
<head>
<meta charset="utf-8">
<title>Silver Brook Custom Homes – Business Card</title>
<link rel="stylesheet" href="https://fonts.googleapis.com/css2?family=Arimo:wght@400;700&family=Cinzel:wght@400&display=swap">
<style>
  :root {
    --bg: #a9a9a9;
    --card-white: #ffffff;
    --green-dark: #4d6b1c;
    --green-text: #55741f;
    --green-back: #4f6c21;
    --green-back-deep: #3e5718;
    --green-light: #b7d36a;
    --ink: #3a3a3a;
  }
  * { box-sizing: border-box; margin: 0; padding: 0; }
  html, body { width: 1200px; height: 800px; overflow: hidden; }
  body {
    background: var(--bg);
    display: flex; align-items: center; justify-content: center; gap: 60px;
    font-family: "Arimo", Arial, sans-serif;
  }
  .card {
    width: 525px; height: 300px; border-radius: 22px; position: relative; overflow: hidden;
  }
  .card-front { background: var(--card-white); color: var(--ink); }
  .brand {
    position: absolute; right: 36px; top: 36px; text-align: center;
    font-family: "Cinzel", serif; color: var(--green-text);
  }
  .brand-mark {
    display: inline-block; width: 14px; height: 14px; border-radius: 50%;
    background: var(--green-text); margin-bottom: 10px;
  }
  .brand-name { font-size: 30px; letter-spacing: 2px; line-height: 1; }
  .brand-sub { font-size: 9px; letter-spacing: 6px; margin-top: 6px; }
  .person { position: absolute; left: 34px; top: 128px; }
  .person-name { font-family: "Cinzel", serif; font-size: 26px; color: var(--green-text); line-height: 1; }
  .person-title { font-size: 13px; margin-top: 6px; }
  .rule {
    position: absolute; left: 34px; right: 34px; top: 184px;
    border-top: 1px solid var(--green-dark);
  }
  .contacts {
    position: absolute; left: 34px; top: 196px; list-style: none;
    font-size: 13px; line-height: 19px;
  }
  .contacts li { display: flex; align-items: center; gap: 8px; }
  .contacts svg { width: 11px; height: 11px; fill: none; stroke: var(--green-dark); stroke-width: 2; }
  .address {
    position: absolute; right: 34px; top: 196px; text-align: right;
    font-size: 13px; line-height: 19px;
  }
  .website {
    position: absolute; right: 34px; top: 256px; text-align: right;
    font-size: 13px; line-height: 19px; font-weight: 700; color: var(--green-dark);
  }
  .card-back {
    background: radial-gradient(circle at 45% 50%, #5f7f29 0%, var(--green-back) 45%, var(--green-back-deep) 100%);
    display: flex; align-items: center; justify-content: center; flex-direction: column;
  }
  .back-mark {
    width: 20px; height: 20px; border-radius: 50%; background: var(--green-light); margin-bottom: 14px;
  }
  .back-name {
    font-family: "Cinzel", serif; font-size: 34px; letter-spacing: 3px; color: var(--green-light);
  }
</style>
</head>
<body>
  <section class="card card-front" aria-label="Business card front">
    <div class="brand">
      <span class="brand-mark"></span>
      <div class="brand-name">Silver Brook</div>
      <div class="brand-sub">CUSTOM HOMES</div>
    </div>
    <div class="person">
      <div class="person-name">DANA PELLMAN</div>
      <div class="person-title">Owner/General Contractor</div>
    </div>
    <div class="rule"></div>
    <ul class="contacts">
      <li><svg viewBox="0 0 12 12"><path d="M2 1 L4 1 L5 4 L3.5 5 Q5 8 7 8.5 L8 7 L11 8 L11 10 Q6 11 2 6 Q1 3 2 1Z"/></svg>555.555.0142</li>
      <li><svg viewBox="0 0 12 12"><rect x="3" y="1" width="6" height="10" rx="1"/></svg>555.555.0178</li>
      <li><svg viewBox="0 0 12 12"><rect x="1" y="2" width="10" height="8"/><path d="M3 6 L5 8 L9 4"/></svg>silverbrookcustomhomes@mailnest.example</li>
    </ul>
    <div class="address">
      <div>218 Wrenfield Mill Road</div>
      <div>Alderwick, ST 29088</div>
    </div>
    <div class="website">silverbrookcustomhomes.example</div>
  </section>
  <section class="card card-back" aria-label="Business card back">
    <span class="back-mark"></span>
    <div class="back-name">SILVER BROOK</div>
  </section>
</body>
</html>
```